Diet, Exercise, & Friends are Associated with Parkinson's disease Progression

We are researchers looking for modifiable variables associated with different rates of Parkinson's disease (PD) progression. This is a novel scale: www.VELKAM.org -- higher scores are associated with worse quality of life. Low is good. High is bad. Each of the dots is a real person (maybe those should disappear?). The line represents the typical rate of PD progression over time. Color scheme of different degrees of quality of life can change, but the general concept seems to be working. (see updated version at the bottom of the www.VELKAM.org website)We need to combine the exercise data from here. This poster was essentially my attempt at an infographic for scientists:https://files.exampledrop.net/static/7a21c4e9b0d3f5a6c8e1d2b4/t/8c33d1a7e5f2b9c4d6a1e7f3/2047719385210/TRV2017+Diet.pdf. The updated data is in the uploaded figure below. Please use this list/ verbage!I don't necessarily need to stick to red=bad, green=good, but that's the best I've been able to come up with to communicate all this. I can get the actual data output later, but it might be nice to be able to demonstrate intensity. Veggies are quite a bit better than spices. Loneliness is much, much worse than pasta. This is the original published data. We have updated data and want to turn it into an infographic (while we work on a new manuscript).https://www.quorvel.net/journals/jrbt/2017/8173920/
Target Market(s)
Individuals age 40-80 with Parkinson's disease (and their friends & family members).
Neurologists should be handing this out in their offices.
When patients ask their physician about nutrition, etc., we want this to be the 1-pg handout they give them.
Industry/Entity Type
Medicine
Font styles to use
Colors
Designer to choose colors to be used in the design.
Requirements
Must have
- VEL-KAM scale (www.VELKAM.org)-- use this picture on top. OK to change color.
- Lists foods/ activities associated with different rates of progression
- Title: "Food, Friends, and Exercise: Lifestyle Associations with PD Progression"
- Legend/ disclaimer (smaller font):
- "All results were adjusted for age, gender, and years since diagnosis. Total sample size: 1600+
- Based on the methods described in publication: "Effects of Meal Timing and Herbal Additives on Tremor Course" [Dunwarth RT et al, Jrnl Biol Tiss Rsch 2017], an updated analysis was performed on data on 7 May 2019. (N >1600)"
- "VEL-KAM scores available at www.VELKAM.org"
- Must fit on a single 8.5 x 11" page.
Nice to have
- The background should be white-- I want neurologists/ physicians downloading it, printing it, and distributing to patients. I don't want to waste ink.
- Logo for Wexmoor College and/or the logo for the "LUN Grove TR" Study. I like the WC emblem in one corner and the picture at the top of this website: www.VELKAM.org
- Would be nice if it could be understood between cultures and/ or easily translated.
- Would be nice if we could invite people to participate in the study!
- "To learn about joining the study, please to www.LUNGroveTR.wexmoor.edu"
Should not have
- Pictures of overweight people, or the impression that a muscular white guy is the ideal. I want to leave room for diversity and flexible interpretation.
- Too much text- a good-sized portion of this group will have poor vision and/or dementia. Needs to be simple.
- I like the simplicity of "Good" and "Bad"... don't love the labels. Seems to 'jugdgy'. Maybe "Encourage" and "Avoid" OR "Positive" and "Negative"

```html
<!DOCTYPE html>
<html lang="en">
<head>
<meta charset="utf-8">
<title>Food, Friends, &amp; Exercise: Lifestyle Associations with PD Progression</title>
<link href="https://fonts.googleapis.com/css2?family=Bebas+Neue&family=Roboto+Condensed:wght@300;400&display=swap" rel="stylesheet">
<style>
  :root {
    --ink: #111;
    --title-blue: #4e4fa3;
    --band-grey: #b3b3b3;
    --poor: #861d0a;
    --fair: #b2674a;
    --good: #5355a2;
    --excellent: #8dcce3;
    --exercise: #7dc31e;
    --encourage: #8dcbe2;
    --avoid: #861d0a;
    --bubble: #e6e6e6;
    --bubble-edge: #a9a9a9;
    --face: #f6c63c;
    --white: #fff;
  }
  * { box-sizing: border-box; margin: 0; padding: 0; }
  html, body { width: 926px; height: 1200px; overflow: hidden; background: var(--white); }
  .page { position: relative; width: 926px; height: 1200px; background: var(--white); font-family: "Roboto Condensed", sans-serif; color: var(--ink); }

  .emblem { position: absolute; top: 45px; width: 109px; height: 109px; border-radius: 50%; display: flex; align-items: center; justify-content: center; text-align: center; font-family: "Bebas Neue", sans-serif; font-size: 19px; line-height: 1; color: var(--white); padding: 12px; }
  .emblem--college { left: 28px; background: var(--poor); }
  .emblem--study { left: 147px; background: var(--good); }

  .title { position: absolute; left: 270px; top: 50px; font-family: "Bebas Neue", sans-serif; font-weight: 400; color: var(--title-blue); font-size: 56px; line-height: 1; letter-spacing: 0.3px; }
  .subtitle { position: absolute; left: 270px; top: 114px; font-family: "Bebas Neue", sans-serif; font-weight: 400; font-size: 41px; line-height: 1; color: var(--ink); white-space: nowrap; }

  .section-band { position: absolute; left: 0; top: 199px; width: 926px; height: 55px; background: var(--band-grey); color: var(--white); font-family: "Bebas Neue", sans-serif; font-size: 38px; letter-spacing: 2px; line-height: 57px; text-align: center; }

  .chart { position: absolute; left: 0; top: 255px; }
  .chart text { font-family: "Roboto Condensed", sans-serif; }

  .notes { position: absolute; left: 696px; top: 298px; width: 199px; font-size: 11.5px; line-height: 16px; text-align: justify; }
  .notes p + p { margin-top: 11px; }

  .bubble { position: absolute; background: var(--bubble); border-radius: 9px; box-shadow: 2px 3px 0 var(--bubble-edge); font-size: 17px; line-height: 1.1; display: flex; align-items: center; justify-content: center; text-align: center; }
  .bubble::after { content: ""; position: absolute; bottom: -10px; border-top: 11px solid var(--bubble); border-left: 9px solid transparent; border-right: 9px solid transparent; }
  .bubble--left::after { left: 10px; }
  .bubble--right::after { right: 10px; }
  .bubble--small { font-size: 14px; line-height: 1.15; }

  .face { position: absolute; width: 56px; height: 56px; border-radius: 50%; background: var(--face); }

  .exercise { position: absolute; left: 326px; top: 634px; width: 274px; height: 529px; background: var(--exercise); border-radius: 16px; padding: 8px; }
  .exercise__frame { width: 100%; height: 100%; border: 3px solid var(--white); border-radius: 12px; color: var(--white); font-family: "Bebas Neue", sans-serif; font-size: 22px; line-height: 25px; text-align: center; padding: 14px 24px 0; }
  .exercise__icon { display: block; margin: 0 auto; width: 40px; height: 40px; border-radius: 6px; background: rgba(255,255,255,0.55); }
  .exercise__icon--top { margin-bottom: 12px; }
  .exercise__frame p { margin-bottom: 25px; }

  .food-list { position: absolute; top: 771px; width: 301px; height: 390px; list-style: none; padding: 6px 10px 0; }
  .food-list--avoid { left: 32px; background: var(--avoid); }
  .food-list--encourage { left: 624px; width: 269px; background: var(--encourage); }
  .food-list li { height: 46.5px; display: flex; align-items: center; color: var(--white); font-size: 21px; font-weight: 300; border-bottom: 1px dashed rgba(255,255,255,0.45); }
  .food-list li:last-child { border-bottom: none; }
  .food-icon { width: 30px; height: 30px; border-radius: 6px; background: rgba(255,255,255,0.35); margin: 0 14px 0 6px; flex: none; }
</style>
</head>
<body>
<main class="page">
  <header>
    <div class="emblem emblem--college">Wexmoor College</div>
    <div class="emblem emblem--study">LUN Grove TR</div>
    <h1 class="title">Food, Friends, &amp; Exercise:</h1>
    <h2 class="subtitle">Lifestyle Associations with PD Progression</h2>
  </header>

  <div class="section-band">Correlation between quality of life &amp; VEL-KAM score</div>

  <svg class="chart" width="690" height="340" viewBox="0 255 690 340" aria-label="VEL-KAM score against years, with quality of life bands">
    <rect x="116" y="286" width="485" height="114" fill="var(--poor)"/>
    <rect x="116" y="400" width="485" height="58" fill="var(--fair)"/>
    <rect x="116" y="458" width="485" height="57" fill="var(--good)"/>
    <rect x="116" y="515" width="485" height="57" fill="var(--excellent)"/>
    <line x1="116" y1="501" x2="575" y2="378" stroke="#000" stroke-width="1.2"/>
    <line x1="116" y1="269" x2="116" y2="572" stroke="#000" stroke-width="1.5"/>
    <line x1="116" y1="572" x2="627" y2="572" stroke="#000" stroke-width="1.5"/>
    <g font-size="13" text-anchor="end">
      <text x="106" y="295">2500</text><text x="106" y="351">2000</text>
      <text x="106" y="407">1500</text><text x="106" y="463">1000</text>
      <text x="106" y="519">500</text><text x="106" y="575">0</text>
    </g>
    <g stroke="#000"><line x1="112" y1="291" x2="120" y2="291"/><line x1="112" y1="347" x2="120" y2="347"/><line x1="112" y1="403" x2="120" y2="403"/><line x1="112" y1="459" x2="120" y2="459"/><line x1="112" y1="515" x2="120" y2="515"/></g>
    <g font-size="13" text-anchor="middle">
      <text x="187" y="593">5</text><text x="256" y="593">10</text><text x="325" y="593">15</text>
      <text x="394" y="593">20</text><text x="463" y="593">25</text><text x="531" y="593">30</text><text x="600" y="593">35</text>
    </g>
    <g stroke="#000"><line x1="187" y1="568" x2="187" y2="576"/><line x1="256" y1="568" x2="256" y2="576"/><line x1="325" y1="568" x2="325" y2="576"/><line x1="394" y1="568" x2="394" y2="576"/><line x1="463" y1="568" x2="463" y2="576"/><line x1="531" y1="568" x2="531" y2="576"/></g>
    <g font-family="Bebas Neue, sans-serif" font-size="22" fill="#fff" text-anchor="end" style="font-family:'Bebas Neue',sans-serif">
      <text x="581" y="355">Poor</text><text x="581" y="440">Fair</text>
      <text x="581" y="500">Good</text><text x="581" y="557">Excellent</text>
    </g>
    <text transform="translate(57 430) rotate(-90)" text-anchor="middle" font-size="30" style="font-family:'Bebas Neue',sans-serif">VEL-KAM Score</text>
    <text transform="translate(642 430) rotate(-90)" text-anchor="middle" font-size="30" style="font-family:'Bebas Neue',sans-serif">Quality of Life</text>
  </svg>

  <aside class="notes">
    <p>All results were adjusted for age, gender, and years since diagnosis. Total sample size: 1600+</p>
    <p>Based on the methods described in publication: "Effects of Meal Timing and Herbal Additives on Tremor Course" [Dunwarth RT et al, Jrnl Biol Tiss Rsch 2017], an updated analysis was performed on data on 7 May 2019. (N &gt;1600)"</p>
    <p>VEL-KAM scores available at www.VELKAM.org</p>
  </aside>

  <div class="bubble bubble--left" style="left:96px;top:634px;width:184px;height:44px;">I am overweight.</div>
  <div class="bubble bubble--left" style="left:114px;top:688px;width:182px;height:45px;">I am lonely</div>
  <div class="face" style="left:31px;top:690px;" role="img" aria-label="Sad emoji"></div>

  <div class="bubble bubble--right bubble--small" style="left:617px;top:631px;width:128px;height:44px;">I try to eat organic<br>when possible</div>
  <div class="bubble bubble--right bubble--small" style="left:762px;top:631px;width:131px;height:44px;">I cook most of<br>my own meals.</div>
  <div class="bubble bubble--right bubble--small" style="left:625px;top:690px;width:183px;height:45px;">I have a lot<br>of friends</div>
  <div class="face" style="left:838px;top:690px;" role="img" aria-label="Happy emoji"></div>

  <section class="exercise">
    <div class="exercise__frame">
      <span class="exercise__icon exercise__icon--top" role="img" aria-label="Dumbbell icon"></span>
      <p>7 days/ week of exercise is better than 6</p>
      <p>6 days/ week of exercise is better than 5...</p>
      <p>Trend continues to 3d/ wk</p>
      <p style="margin-bottom:10px">No benefit associated with 0-2 days/ wk</p>
      <span class="exercise__icon" role="img" aria-label="Bicycle and tree icon"></span>
    </div>
  </section>

  <ul class="food-list food-list--avoid" aria-label="Avoid">
    <li><span class="food-icon" role="img" aria-label="Cheese icon"></span>Dairy</li>
    <li><span class="food-icon" role="img" aria-label="Steak icon"></span>Beef</li>
    <li><span class="food-icon" role="img" aria-label="Roast chicken icon"></span>Chicken</li>
    <li><span class="food-icon" role="img" aria-label="Fries icon"></span>Fried food</li>
    <li><span class="food-icon" role="img" aria-label="Tin can icon"></span>Canned food</li>
    <li><span class="food-icon" role="img" aria-label="Canned vegetables icon"></span>Canned vegatables</li>
    <li><span class="food-icon" role="img" aria-label="Snowflake icon"></span>Frozen vegatables</li>
    <li><span class="food-icon" role="img" aria-label="Soda can icon"></span>Soda</li>
  </ul>

  <ul class="food-list food-list--encourage" aria-label="Encourage">
    <li><span class="food-icon" role="img" aria-label="Herb leaf icon"></span>Fresh herbs</li>
    <li><span class="food-icon" role="img" aria-label="Olive oil icon"></span>Olive &amp; Coconut oil</li>
    <li><span class="food-icon" role="img" aria-label="Nuts icon"></span>Nuts &amp; Seeds</li>
    <li><span class="food-icon" role="img" aria-label="Spices icon"></span>Spices</li>
    <li><span class="food-icon" role="img" aria-label="Fish icon"></span>Non-Fried fish</li>
    <li><span class="food-icon" role="img" aria-label="Mushrooms icon"></span>Fresh food</li>
    <li><span class="food-icon" role="img" aria-label="Carrot icon"></span>Fresh vegatables</li>
    <li><span class="food-icon" role="img" aria-label="Wine glass icon"></span>Wine</li>
  </ul>
</main>
</body>
</html>
```